Business Card Design Project : Tidewell Press

In preparation for market launch, Whistler's Tidewell Press require the development of a business card. Tidewell Press is a Community online publishing web portal. We provide the the city of Whistler located in B.C. (Canada) business directories, News, Classified ads, News, Events and blogs etc.

The main focus of the brand is to help local businesses to corporate with their online advertisement and marketing. Meeting our clients face to face is a must (B2B).

Target Market(s)

The target market is B2B customers. Business Owners to Marketing, advertising Managers

Industry/Entity Type

Business

Requirements
Must have
• - The business card will be two sided.
the BACK side will have our logo which consist of (icon, url,slogan) submited. The logo will be middle and centred.

The FRONT side should have company details:

Company Legal Name: FERNDALE TIDEWELL PRESS

Owen Marsk
Director of Sales & Marketing

www.ferndaletidewell.biz
owen@ferndaletidewell.biz

Phone: 555 014 3826
#2817 - 562 E. Harlow Ave.
Vancouver, B.C. K7P2R4 Canada
Nice to have
• - For the "FRONT" side of our business card. You can separate or re-arrange with our logo components (icon, logo,slogan). It does not have to be together.

Also our company legal name is rather long so arrange or organize the name in a way to make it shorter. Your experience and creativity will have to come in play.
Should not have
• should not have other colors beside logo color and black text (2 colors). Also nothing Three dimensional

```html
<!DOCTYPE html>
<html lang="en">
<head>
<meta charset="utf-8">
<title>Ferndale Tidewell Press – Business Card</title>
<link rel="stylesheet" href="https://fonts.googleapis.com/css2?family=Arimo:wght@400;700&family=Open+Sans:wght@400;700&display=swap">
<style>
  :root {
    --brand-blue: #3b93eb;
    --ink: #111111;
    --paper: #ffffff;
    --card-border: #222222;
  }
  html, body {
    margin: 0;
    padding: 0;
    overflow: hidden;
    background: var(--paper);
  }
  .canvas {
    position: relative;
    width: 1200px;
    height: 800px;
    overflow: hidden;
    background: var(--paper);
    font-family: "Arimo", Arial, sans-serif;
    color: var(--ink);
  }
  .side-label {
    position: absolute;
    top: 182px;
    width: 530px;
    margin: 0;
    text-align: center;
    font-family: "Open Sans", Arial, sans-serif;
    font-weight: 400;
    font-size: 27px;
    letter-spacing: 0.5px;
    color: var(--ink);
  }
  .side-label--front { left: 57px; }
  .side-label--back { left: 620px; }

  .card {
    position: absolute;
    top: 240px;
    width: 528px;
    height: 322px;
    border: 1.5px solid var(--card-border);
    background: var(--paper);
    overflow: hidden;
  }
  .card--front { left: 57px; }
  .card--back { left: 620px; }

  /* Front side */
  .card__swoosh {
    position: absolute;
    inset: 0;
    width: 100%;
    height: 100%;
  }
  .card__company-ribbon {
    font-family: "Arimo", Arial, sans-serif;
    font-weight: 700;
    font-size: 17px;
    fill: var(--ink);
  }
  .person {
    position: absolute;
    left: 16px;
    top: 8px;
  }
  .person__name {
    margin: 0;
    font-weight: 700;
    font-size: 33px;
    line-height: 40px;
  }
  .person__title {
    margin: 6px 0 0;
    font-weight: 700;
    font-size: 13px;
  }
  .contact {
    position: absolute;
    left: 260px;
    top: 186px;
    font-weight: 700;
    font-size: 14.5px;
    line-height: 19.5px;
    font-style: normal;
  }
  .contact p { margin: 0; }
  .contact__online { margin-top: 15px !important; }

  /* Back side */
  .brand-lockup {
    position: absolute;
    left: 0;
    right: 0;
    top: 70px;
    text-align: center;
  }
  .brand-lockup__mark {
    display: block;
    width: 78px;
    height: 78px;
    margin: 0 auto;
    border-radius: 50%;
    background: var(--brand-blue);
  }
  .brand-lockup__url {
    margin: 20px 0 0;
    font-family: "Open Sans", Arial, sans-serif;
    font-weight: 700;
    font-size: 34px;
    line-height: 40px;
    letter-spacing: -0.5px;
    color: var(--ink);
  }
  .brand-lockup__slogan {
    margin: 0;
    font-family: "Open Sans", Arial, sans-serif;
    font-weight: 400;
    font-size: 24px;
    line-height: 30px;
    color: var(--brand-blue);
  }
</style>
</head>
<body>
<main class="canvas">
  <h2 class="side-label side-label--front">FRONT</h2>
  <h2 class="side-label side-label--back">BACK</h2>

  <section class="card card--front" aria-label="Business card front">
    <svg class="card__swoosh" viewBox="0 0 397 243" preserveAspectRatio="none" aria-hidden="false">
      <path d="M -15 250 C 70 185, 140 95, 225 78 S 345 74, 402 26"
            fill="none" stroke="var(--brand-blue)" stroke-width="30" stroke-linecap="butt"/>
      <text class="card__company-ribbon" x="11" y="224" transform="rotate(-36 11 224)"
            textLength="258" lengthAdjust="spacingAndGlyphs">Ferndale Tidewell Press</text>
    </svg>

    <div class="person">
      <h1 class="person__name">Owen Marsk</h1>
      <p class="person__title">Director of Sales and Marketing</p>
    </div>

    <address class="contact">
      <p>Phone: 555 014 3826</p>
      <p>#2817 - 562 E. Harlow Ave.</p>
      <p>Vancouver, B.C. K7P2R4 Canada</p>
      <p class="contact__online">www.ferndaletidewell.biz</p>
      <p>owen@ferndaletidewell.biz</p>
    </address>
  </section>

  <section class="card card--back" aria-label="Business card back">
    <div class="brand-lockup">
      <span class="brand-lockup__mark" aria-hidden="true"></span>
      <p class="brand-lockup__url">www.ferndaletidewell.biz</p>
      <p class="brand-lockup__slogan">Your information gateway</p>
    </div>
  </section>
</main>
</body>
</html>
```